Powerpoint Template needed for new Digital Consultancy

We have recently had our logo designed through Sketchmarket and would now like to extend the brand look & feel through to having a powerpoint template created that we can use as a master template within which to create our client presentations.
Typical slides required and in terms of what we would need templating is:

- Stylised header and footer for main content slides
- intro/front page slide
- contents page slide
- standardised font type and sizes, heading types (including sizes) for Level 1, Level 2 and Level 3 headings
- use of text colour and any standards/styling around when to use bold, underline, italics etc
- table styling for when we want to use tables in the presentation
- standards and styles around using bullet and number lists
- stylising use of imagery that is dropped in e.g. do all images have a certain border style or drop-shadow etc.
- style and slide layout/format for how team profiles are handled
- style and slide layout/format for how case studies are handled
- closing, contact-us page

We can send over logo files and colour/font styles etc used for the logo soon.

Target Market(s)

B2B professional clients that are either medium to large corporations or potentially some government departments.

Industry/Entity Type

Digital

Font styles to use
Sans Serif

Colors
ec1f27
f37122
f78f20
faa54b
f68d4d
0255a3

Requirements
Must have
• Ideally as many templated pages/master slide types as outlined above in the brief to meet the requirements of what the powerpoint deck will be used for. Namely client presentations and pitches.
• Versions of the logo are attached to give an idea of the colour palette and clean, modern style we are looking for, plus the type of font we are using and like.
• We are looking for the slide design to be modern, minimalistic, clean and not overuse of colour. Preferably a white slide background so it's easy to then read slide content when we populate the slides with text which will be in black.
Nice to have
• Not expecting to see too much more than simple use of the logo and a slide header perhaps using some sort of line as a break and then a simple footer as well.
• Consider using Abode font.
Should not have
• Too much block colour or elements that draw away from what will go in the main content body of our slides when we use them.

```html
<!DOCTYPE html>
<html lang="en">
<head>
<meta charset="utf-8">
<title>Contents</title>
<link rel="stylesheet" href="https://fonts.googleapis.com/css2?family=Arimo:wght@400;700&display=swap">
<style>
  :root {
    --navy-deep: #0a2240;
    --navy-soft: #1b3a5e;
    --tab: #f9a54b;
    --tab-fold: #c77a2a;
    --white: #ffffff;
    --ink: #111111;
  }
  * { margin: 0; padding: 0; box-sizing: border-box; }
  html, body { width: 1200px; height: 900px; overflow: hidden; background: var(--white); }
  .slide {
    position: relative;
    width: 1200px;
    height: 900px;
    background: var(--white);
    font-family: "Arimo", Arial, sans-serif;
    overflow: hidden;
  }
  .slide-title {
    position: absolute;
    left: 26px;
    top: 18px;
    font-size: 52px;
    font-weight: 700;
    color: var(--navy-deep);
    letter-spacing: -0.5px;
  }
  .contents-list { list-style: none; }
  .contents-item {
    position: absolute;
    left: 28px;
    width: 1155px;
    height: 70px;
    background: linear-gradient(to bottom, var(--navy-deep) 0 50%, var(--navy-soft) 50% 100%);
  }
  .contents-item:nth-child(1) { top: 148px; }
  .contents-item:nth-child(2) { top: 277px; }
  .contents-item:nth-child(3) { top: 403px; }
  .contents-item:nth-child(4) { top: 532px; }
  .contents-item:nth-child(5) { top: 658px; }
  .section-label {
    position: absolute;
    left: 14px;
    top: 50%;
    transform: translateY(-50%);
    font-size: 30px;
    font-weight: 700;
    color: var(--white);
  }
  .page-tab {
    position: absolute;
    left: 1052px;
    top: -15px;
    width: 87px;
    height: 87px;
    background: var(--tab);
    color: var(--ink);
    font-size: 28px;
    font-weight: 700;
    text-align: center;
    padding-top: 18px;
    box-shadow: 2px 2px 4px rgba(0,0,0,0.25);
  }
  .tab-fold {
    position: absolute;
    left: 1038px;
    top: -15px;
    width: 14px;
    height: 15px;
  }
  .footer-band {
    position: absolute;
    left: 0;
    bottom: 0;
    width: 1200px;
    height: 170px;
  }
  .page-number {
    position: absolute;
    left: 22px;
    bottom: 14px;
    font-size: 16px;
    color: var(--white);
  }
  .brand-name {
    position: absolute;
    right: 20px;
    bottom: 14px;
    font-size: 24px;
    font-weight: 700;
    color: var(--white);
  }
</style>
</head>
<body>
  <main class="slide">
    <h1 class="slide-title">Contents</h1>

    <ol class="contents-list">
      <li class="contents-item">
        <span class="section-label">Section 1</span>
        <svg class="tab-fold" viewBox="0 0 14 15" aria-hidden="true"><polygon points="14,0 14,15 0,15" fill="var(--tab-fold)"/></svg>
        <span class="page-tab">#</span>
      </li>
      <li class="contents-item">
        <span class="section-label">Section 2</span>
        <svg class="tab-fold" viewBox="0 0 14 15" aria-hidden="true"><polygon points="14,0 14,15 0,15" fill="var(--tab-fold)"/></svg>
        <span class="page-tab">#</span>
      </li>
      <li class="contents-item">
        <span class="section-label">Section 3</span>
        <svg class="tab-fold" viewBox="0 0 14 15" aria-hidden="true"><polygon points="14,0 14,15 0,15" fill="var(--tab-fold)"/></svg>
        <span class="page-tab">#</span>
      </li>
      <li class="contents-item">
        <span class="section-label">Section 4</span>
        <svg class="tab-fold" viewBox="0 0 14 15" aria-hidden="true"><polygon points="14,0 14,15 0,15" fill="var(--tab-fold)"/></svg>
        <span class="page-tab">#</span>
      </li>
      <li class="contents-item">
        <span class="section-label">Section 5</span>
        <svg class="tab-fold" viewBox="0 0 14 15" aria-hidden="true"><polygon points="14,0 14,15 0,15" fill="var(--tab-fold)"/></svg>
        <span class="page-tab">#</span>
      </li>
    </ol>

    <footer>
      <svg class="footer-band" viewBox="0 0 1200 170" aria-hidden="true">
        <polygon points="0,120 990,120 1200,2 1200,170 0,170" fill="var(--navy-deep)"/>
      </svg>
      <span class="page-number">3</span>
      <span class="brand-name">Halden Digital</span>
    </footer>
  </main>
</body>
</html>
```